A simple and smart interface for busy teachers

We have an existing app (hybrid) on Apple Appstore and Google Playstore that we wish to refresh with some awesome designs and simplified screens.

We would like to stick to our existing colour scheme, see our website plovano.co.nz or screenshots on the appstore for more details and use of colours.

The uploaded files are current screens that we would like redesigned. Specifically, here are additional thoughts on what we wish to see:
1. With the Active Jobs screen, we would prefer to see a week-ly calendar style layout.
2. With Favourites, we would like to see each person's availability going across the page.

Target Market(s)

Middle aged women. (40+). New to tech users.

Industry/Entity Type

Education

Number of Pages Required

5+ page

Font styles to use
Sans Serif

Colors
ec1f27
474747
f78f20

Requirements
Must have
• Calendar view.
• Tidy and sharp info about the jobs.
Nice to have
• Simple and sharp.
Should not have
• Complicated graphics.
• Cluttered designs.
• Too much red. Screens should be mainly white(ish) with red and black.

```html
<!DOCTYPE html>
<html lang="en">
<head>
<meta charset="utf-8">
<title>Plovano – Welcome</title>
<link rel="stylesheet" href="https://fonts.googleapis.com/css2?family=Roboto:wght@300;400;500&display=swap">
<style>
  :root {
    --red: #ec1f27;
    --charcoal: #474747;
    --orange: #f78f20;
    --white: #ffffff;
    --bg-top: #ffffff;
    --bg-bottom: #ededed;
    --ink: #222222;
    --muted: #5a5a5a;
    --icon-grey: #d8d8d8;
  }
  * { margin: 0; padding: 0; box-sizing: border-box; }
  html, body { width: 800px; height: 1200px; overflow: hidden; }
  body {
    font-family: "Roboto", Arial, sans-serif;
    background: linear-gradient(to bottom, var(--bg-top) 0%, var(--bg-top) 40%, var(--bg-bottom) 100%);
    position: relative;
  }
  .brand {
    position: absolute;
    top: 100px;
    left: 0;
    width: 800px;
    text-align: center;
  }
  .brand-dot {
    display: block;
    width: 210px;
    height: 210px;
    margin: 0 auto;
    border-radius: 50%;
    background: var(--red);
  }
  .brand-name {
    display: block;
    margin-top: 28px;
    font-size: 78px;
    font-weight: 400;
    line-height: 1;
    color: var(--red);
    letter-spacing: 1px;
  }
  .brand-tagline {
    display: block;
    margin-top: 10px;
    font-size: 21px;
    font-weight: 400;
    color: var(--ink);
  }
  .actions {
    position: absolute;
    top: 598px;
    left: 152px;
    width: 498px;
    list-style: none;
  }
  .action {
    display: flex;
    height: 114px;
    margin-bottom: 29px;
    border-radius: 6px;
    overflow: hidden;
    color: var(--white);
    text-decoration: none;
  }
  .action--login { background: var(--charcoal); }
  .action--register { background: var(--red); }
  .action--help { background: var(--orange); }
  .action-icon {
    width: 100px;
    display: flex;
    align-items: center;
    justify-content: center;
    border-right: 2px solid rgba(0,0,0,0.12);
  }
  .action-icon svg { width: 38px; height: 38px; }
  .action-label {
    flex: 1;
    display: flex;
    align-items: center;
    justify-content: center;
    padding-right: 70px;
    font-size: 33px;
    font-weight: 400;
    letter-spacing: 0.5px;
  }
  .footer {
    position: absolute;
    top: 1112px;
    left: 100px;
    width: 690px;
    display: flex;
    justify-content: space-between;
    font-size: 29px;
    font-weight: 300;
    color: var(--muted);
  }
</style>
</head>
<body>
  <header class="brand">
    <span class="brand-dot"></span>
    <span class="brand-name">plovano</span>
    <span class="brand-tagline">staff on demand</span>
  </header>

  <ul class="actions">
    <li>
      <a class="action action--login" href="#">
        <span class="action-icon">
          <svg viewBox="0 0 24 24" aria-hidden="true">
            <path d="M7 11V8a5 5 0 0 1 10 0v3" fill="none" stroke="var(--icon-grey)" stroke-width="2.6"/>
            <rect x="4.5" y="11" width="15" height="11" rx="1.5" fill="var(--icon-grey)"/>
          </svg>
        </span>
        <span class="action-label">LOGIN</span>
      </a>
    </li>
    <li>
      <a class="action action--register" href="#">
        <span class="action-icon">
          <svg viewBox="0 0 24 24" aria-hidden="true">
            <path d="M5 2h10l5 5v15H5z" fill="var(--white)"/>
            <path d="M15 2v5h5" fill="var(--red)" opacity="0.35"/>
            <rect x="8" y="11" width="9" height="1.8" fill="var(--red)"/>
            <rect x="8" y="14.5" width="9" height="1.8" fill="var(--red)"/>
            <rect x="8" y="18" width="9" height="1.8" fill="var(--red)"/>
          </svg>
        </span>
        <span class="action-label">REGISTER</span>
      </a>
    </li>
    <li>
      <a class="action action--help" href="#">
        <span class="action-icon">
          <svg viewBox="0 0 24 24" aria-hidden="true">
            <circle cx="12" cy="12" r="11" fill="var(--white)"/>
            <path d="M8.8 9.2a3.2 3.2 0 1 1 4.6 2.9c-1 .5-1.4 1.1-1.4 2.2v.6" fill="none" stroke="var(--orange)" stroke-width="2.6" stroke-linecap="round"/>
            <circle cx="12" cy="18.3" r="1.6" fill="var(--orange)"/>
          </svg>
        </span>
        <span class="action-label">HELP</span>
      </a>
    </li>
  </ul>

  <footer class="footer">
    <span class="footer-copy">© 2015 Company Name | All Rights Reserved</span>
    <span class="footer-screen">C5</span>
  </footer>
</body>
</html>
```